Packaging label for spirit line

We currently have a various line of spirits and are looking to rebrand the label. The bottle would stay the same since there is a lot of stock. An example of the current situation has been attached. The entire collection is to be found on our website: www.velvetparlor.quinmark.be/spirits

These spirits are a product created by our cocktail bar "Velvet Parlor". The name however, would likely change to "Tipplefox" or plural "Tipplefoxes" since we'd like to split those 2 businesses. The series "shaker lineup" would remain the same as it is a complete series mainly invented for mixology.

The current label is fine, but needs that extra spark that makes it stand out on a shelve compared to other spirit bottles. We envision a more funky yet sophisticated branding with perhaps goldtrims for that "exclusive, luxurious" feel and very much like a vintage animal humification vibe (for example: the marigold or fennick's). Preferably a french bulldog as this has been our mascotte since the very beginning of starting this business.

Last but not least, the measurements: max. 90 mm height and max. 260 mm length. The current label is 90x180mm. 260mm means the label goes fully around the bottle.

Industry/Entity Type

Alcoholic Beverages

Font styles to use
Serif
Sans Serif

Requirements
Must have
• The label must have the standard information such as the product name, the alcohol %, the volume ml and room for ean code. The bottle needs to be sealed for shipment, so a little seal to cover the lid is required.
Nice to have
• It would be nice to maintain consistency with for example the same animal but change of background / colors / outfit / etc to clarify the different flavors. A cutout/contour is also preferable for added interest, so that the label is not square.
Should not have
• The label should definitely not be childish or too much. The overal look and feel needs to be professional yet not too serious.

```html
<!DOCTYPE html>
<html lang="en">
<head>
<meta charset="utf-8">
<title>Tipplefox Spirit Labels</title>
<link href="https://fonts.googleapis.com/css2?family=Marcellus&family=Montserrat:wght@300;400&display=swap" rel="stylesheet">
<style>
  :root {
    --canvas: #f3f3f3;
    --label: #f7f7f7;
    --ink: #111111;
    --rule: #222222;
    --blush: #f2a69c;
    --blush-soft: #f6cfc8;
    --sage: #7f9a45;
    --sage-soft: #c9d6ad;
  }
  * { box-sizing: border-box; margin: 0; padding: 0; }
  html, body { width: 1200px; height: 1200px; overflow: hidden; }
  body {
    background: var(--canvas);
    position: relative;
    font-family: "Montserrat", sans-serif;
    color: var(--ink);
  }
  .label {
    position: absolute;
    top: 380px;
    width: 352px;
    height: 440px;
    background: var(--label);
    box-shadow: 0 1px 4px rgba(0,0,0,0.12);
  }
  .label--triple-sec { left: 174px; }
  .label--gin { left: 674px; }

  .mascot-art {
    position: absolute;
    top: 14px;
    left: 76px;
    width: 200px;
    height: 120px;
    border-radius: 4px;
  }
  .label--triple-sec .mascot-art { background: linear-gradient(90deg, var(--blush-soft), #ececec 35%, #ececec 65%, var(--blush-soft)); }
  .label--gin .mascot-art { background: linear-gradient(90deg, var(--sage-soft), #ececec 35%, #ececec 65%, var(--sage-soft)); }

  .brand {
    position: absolute;
    top: 140px;
    width: 100%;
    text-align: center;
    font-family: "Marcellus", serif;
    font-size: 23px;
    letter-spacing: 0.5px;
  }
  .brand-rule {
    position: absolute;
    top: 173px;
    left: 131px;
    width: 90px;
    height: 1px;
    background: var(--rule);
  }

  .product-name {
    position: absolute;
    top: 180px;
    width: 100%;
    font-weight: 300;
    line-height: 1;
  }
  .label--triple-sec .line-1 { display: block; text-align: center; color: var(--blush); font-size: 48px; letter-spacing: 1px; padding-left: 28px; }
  .label--triple-sec .line-2 { display: block; text-align: right; padding-right: 78px; font-size: 64px; font-weight: 400; margin-top: 2px; }

  .label--gin .line-1 { display: block; text-align: center; color: var(--sage); font-size: 46px; letter-spacing: 1px; margin-top: 2px; }
  .label--gin .line-2 { display: flex; align-items: flex-end; justify-content: center; margin-top: 2px; }
  .label--gin .word-dry { font-size: 42px; font-weight: 300; margin-bottom: 16px; }
  .label--gin .word-gin { font-size: 66px; font-weight: 400; }

  .tagline {
    position: absolute;
    top: 296px;
    width: 100%;
    text-align: center;
    font-size: 21px;
    letter-spacing: 6px;
    padding-left: 6px;
  }
  .label--triple-sec .tagline { color: var(--blush); }
  .label--gin .tagline { color: var(--sage); font-weight: 400; }

  .info-panel {
    position: absolute;
    top: 340px;
    left: 44px;
    width: 264px;
    height: 86px;
    border: 1px solid var(--rule);
    display: grid;
    grid-template-columns: 48px 1fr;
    grid-template-rows: 25px 14px 1fr;
    font-family: "Marcellus", serif;
  }
  .label--gin .info-panel { top: 336px; }
  .info-title {
    grid-column: 1 / 3;
    text-align: center;
    font-size: 19px;
    line-height: 25px;
    border-bottom: 1px solid var(--rule);
  }
  .info-number {
    grid-row: 2 / 4;
    border-right: 1px solid var(--rule);
    position: relative;
  }
  .info-number .no { position: absolute; top: 2px; left: 4px; font-size: 9px; }
  .info-number .digit { position: absolute; bottom: 0; right: 8px; font-size: 38px; line-height: 1; }
  .label--triple-sec .digit { color: var(--blush); }
  .label--gin .digit { color: var(--sage); }
  .info-kind {
    font-family: "Montserrat", sans-serif;
    font-size: 8px;
    letter-spacing: 1.6px;
    text-align: center;
    line-height: 13px;
    border-bottom: 1px solid var(--rule);
  }
  .info-volume {
    text-align: center;
    font-size: 15px;
    line-height: 44px;
  }
</style>
</head>
<body>
  <section class="label label--triple-sec">
    <div class="mascot-art" role="img" aria-label="Line drawing of a French bulldog in a suit and bow tie framed by blush orange branches"></div>
    <div class="brand">TIPPLEFOX</div>
    <div class="brand-rule"></div>
    <h1 class="product-name">
      <span class="line-1">TRIPLE</span>
      <span class="line-2">SEC</span>
    </h1>
    <p class="tagline">DRY CURAÇAO</p>
    <div class="info-panel">
      <div class="info-title">DRY CURAÇAO</div>
      <div class="info-number"><span class="no">NO.</span><span class="digit">3</span></div>
      <div class="info-kind">ORANGE LIQUEUR</div>
      <div class="info-volume">500ML 37.0% VOL. ALC.</div>
    </div>
  </section>

  <section class="label label--gin">
    <div class="mascot-art" role="img" aria-label="Line drawing of a French bulldog in a suit and bow tie framed by green herb sprigs"></div>
    <div class="brand">TIPPLEFOX</div>
    <div class="brand-rule"></div>
    <h1 class="product-name">
      <span class="line-1">LONDON</span>
      <span class="line-2"><span class="word-dry">DRY</span><span class="word-gin">GIN</span></span>
    </h1>
    <p class="tagline">WILDSPRIG</p>
    <div class="info-panel">
      <div class="info-title">WILDSPRIG</div>
      <div class="info-number"><span class="no">NO.</span><span class="digit">1</span></div>
      <div class="info-kind">DISTILLED SPIRIT</div>
      <div class="info-volume">500ML 30.0% VOL.ALC.</div>
    </div>
  </section>
</body>
</html>
```